Pinecrest Treatment Brochure for a drug and alcohol addiction treatment center.

***Update #2***
For graphic highlights no intrusion into text and no fade into adjoining areas.Use modern clean white layout with grey and light orange color scheme. Use attached yoga photo and other photos. For cover try moving number and logo around, and also try with cover photo not full size. Also use larger text with bullet points in a couple spots. Also try with new attached cover photos.
***Update*** I have attached some new photos to clarify the design wanted. My client likes the size (but not design) of the brochure in the newly included photos. Note the measurements - when closed it is 6" wide x 7" tall. When fully open it is 18" long, 7" wide, with 2 folds. I apologize if my terminology below was confusing. Please confirm that your design reflects the desired layout, and please modify your design if it does not. Thanks!
Want a trifold brochure 6" wide x 7" height. Design is for a drug and alcohol addiction treatment center. We want clean, soft, contemporary with highlight colors orange and grey, with contemporary font. Maybe some soft curves on design - see this A4 design we like but not the colors:
http://stockmosaic.example/item/corporate-folded-leaflet-ripple/7391052?s_phrase=trifold%20business%20brochure&s_rank=54
See company web site for style cues and some content you can use:
http://pinecrestcarehub.example/
You can use the attached photos and logo in the design. Try sun in hand photo on cover, or man on beach. Please do not use the words "The Pinecrest Treatment Center" in verbiage or titles, for business reasons we want to use "Pinecrest Treatment Center" with no "The" instead.
Please note that the logo has been updated. The new logo is attached below. Use pinecrest rev2.png for logo.
Addiction treatment industry professionals; family and decision makers of addict; addict themselves.
Health And Wellness

```html
<!DOCTYPE html>
<html lang="en">
<head>
<meta charset="utf-8">
<title>Pinecrest Treatment Center – Trifold Brochure</title>
<link rel="stylesheet" href="https://fonts.googleapis.com/css2?family=Jost:wght@400;500&family=Lato:ital,wght@0,400;0,700;0,900;1,700&display=swap">
<style>
  :root{
    --orange:#f07c1a;
    --orange-light:#f7a23a;
    --charcoal:#2b2b2b;
    --charcoal-2:#3d3d3d;
    --ink:#222;
    --body:#333;
    --white:#fff;
    --stage:#e9e6e2;
  }
  *{margin:0;padding:0;box-sizing:border-box}
  html,body{width:1200px;height:537px;overflow:hidden;background:var(--stage)}
  .brochure{
    position:absolute;left:20px;top:43px;width:1263px;height:490px;
    transform:scale(0.9184);transform-origin:0 0;
    background:var(--white);overflow:hidden;
    font-family:"Lato",sans-serif;color:var(--body);
    box-shadow:0 6px 18px rgba(0,0,0,.25);
  }
  .panel-inside{position:absolute;left:422px;top:0;width:420px;height:490px;
    background:linear-gradient(160deg,var(--charcoal-2),var(--charcoal))}
  .cover-photo{position:absolute;left:842px;top:40px;width:421px;height:400px;
    background:linear-gradient(180deg,#f3b64a 0%,#f6c661 28%,#d98a2a 42%,#4d6e78 50%,#6c7d7a 60%,#c98a3a 74%,#3a2a1a 100%)}
  .waves{position:absolute;inset:0;width:1263px;height:490px}
  .about-title{position:absolute;left:17px;top:86px;font:400 20px "Jost",sans-serif;color:var(--ink)}
  .about-body{position:absolute;left:18px;top:126px;width:386px;font-size:9.6px;line-height:11.7px;text-align:justify;color:var(--body)}
  .about-body p{margin-bottom:4px}
  .tagline{position:absolute;left:114px;top:371px;font:italic 700 14.5px/19px "Lato",sans-serif;color:var(--ink)}
  .service-title{position:absolute;left:441px;font:400 20px "Jost",sans-serif;color:var(--orange-light)}
  .service-body{position:absolute;left:442px;width:231px;font-size:9.4px;line-height:11.8px;text-align:justify;color:var(--white)}
  .service-photo{position:absolute;left:689px;width:134px;height:104px;border:3px solid var(--orange);border-radius:11px;overflow:hidden}
  .photo-beach{top:86px;background:linear-gradient(180deg,#7fa7c9 0%,#c7d8e6 45%,#2f4f6a 60%,#1f3346 100%)}
  .photo-yoga{top:221px;background:linear-gradient(180deg,#6a6fb8 0%,#b18ac6 45%,#e9a9b8 62%,#3a3550 100%)}
  .contact-pill{position:absolute;left:588px;top:376px;width:78px;height:17px;border-radius:9px;background:var(--orange);color:var(--white);font-size:12px;line-height:17px;text-align:center}
  .contact-line{position:absolute;left:420px;width:420px;text-align:center;color:var(--white);font-size:13px}
  .contact-line svg{vertical-align:-1px;margin-right:7px}
  .logo{position:absolute;left:884px;top:76px;display:flex;align-items:center;gap:8px}
  .logo-dot{width:22px;height:22px;border-radius:50%;background:var(--ink)}
  .logo-name{font:900 11px/12px "Lato",sans-serif;color:var(--ink);text-transform:uppercase}
  .cover-title{position:absolute;left:842px;top:318px;width:421px;text-align:center}
  .cover-title .name{display:block;font:900 45px/52px "Lato",sans-serif;color:var(--orange)}
  .cover-title .sub{display:block;font:900 24px/28px "Lato",sans-serif;color:var(--white);letter-spacing:.5px}
  .cover-url{position:absolute;left:842px;top:455px;width:421px;text-align:center;color:var(--white);font-size:12.5px;letter-spacing:2px}
</style>
</head>
<body>
<main class="brochure">
  <div class="panel-inside"></div>
  <div class="cover-photo" role="img" aria-label="Photo of a man standing on a beach at sunset, silhouetted against the golden sea"></div>

  <svg class="waves" viewBox="0 0 1263 490" aria-hidden="true">
    <path d="M0 0H1263V58C1120 40 1000 30 842 38C650 48 430 20 0 44Z" fill="var(--orange)"/>
    <path d="M0 44C430 20 650 48 842 38C1000 30 1120 40 1263 58V62C1120 46 1000 40 842 46C650 56 430 30 0 52Z" fill="var(--white)"/>
    <path d="M0 54C200 40 330 40 420 46C300 48 150 58 0 70Z" fill="var(--charcoal)"/>
    <path d="M842 46C1000 40 1120 48 1263 64V78C1120 56 1000 52 842 52Z" fill="var(--charcoal)"/>
    <path d="M0 422C150 414 300 428 422 440C300 434 150 432 0 446Z" fill="var(--orange)"/>
    <path d="M0 446C150 432 300 434 422 440V490H0Z" fill="var(--charcoal)"/>
    <path d="M422 446C560 452 700 458 842 446V452C700 464 560 458 422 452Z" fill="var(--white)" opacity=".9"/>
    <path d="M842 440C1000 420 1130 414 1263 412V420C1130 424 1000 432 842 446Z" fill="var(--orange)"/>
    <path d="M842 446C1000 432 1130 424 1263 420V490H842Z" fill="var(--charcoal)"/>
  </svg>

  <section class="panel-about">
    <h2 class="about-title">About us</h2>
    <div class="about-body">
      <p>Pinecrest Treatment Center offers affordable treatment for a wide variety of addictions. We address underlying psychological disorders and specialize in treatment for drug addiction and alcoholism. At Pinecrest Treatment Center we feature a full spectrum of addiction treatment programs, from initial assessment and detox, to inpatient residential and intensive outpatient care, as well as transitional housing and sober living environments for extended care.</p>
      <p>Our clinical team are committed to treating each client with respect and are receptive to each clients’ individual needs. Our treatment programs are abstinence based. We provide a comprehensive slate of services, such as individual, group counseling, drug and alcohol educational groups, and an introduction to 12-step programs. We also offer a strong family support program, recognizing the special importance of family healing in the recovery process.</p>
      <p>At Pinecrest Treatment Center we believe strongly in a holistic approach to recovery through treating the mind, body, and soul. To facilitate this holistic recovery perspective we promote a healthy diet for our clients, and physical fitness through visits to a nationally recognized gym. In addition, guided yoga and meditation, hiking trips in Southern California’s beautiful natural areas, and trips to the areas world-famous beaches are available during a client’s stay.</p>
    </div>
    <p class="tagline">Pinecrest Treatment Center<br>– Recover from Addiction</p>
  </section>

  <section class="panel-services">
    <h3 class="service-title" style="top:78px">Alcohol Rehab</h3>
    <p class="service-body" style="top:113px">Pinecrest Treatment Center offers a contemporary approach to recovery from alcoholism. We recognize the necessity of treating the underlying issues from a psychological perspective, combining this with time-tested methods such as 12 step programs, and creating a synergy between these with a holistic approach to the individual.</p>
    <div class="service-photo photo-beach" role="img" aria-label="Photo of a man with outstretched arms on the shore under a blue sky"></div>

    <h3 class="service-title" style="top:211px">Drug Addiction Rehab</h3>
    <p class="service-body" style="top:251px">At Pinecrest Treatment Center we specialize in treatment of addiction for the entire spectrum of drugs that are abused in our contemporary society. Our nationally renowned clinical team has experience with treating addiction to all types of substances, while at the same time recognizing the unique nature of each individual client.</p>
    <div class="service-photo photo-yoga" role="img" aria-label="Photo of a woman in a yoga pose silhouetted against a purple sunset"></div>

    <div class="contact-pill">Contact Us</div>
    <p class="contact-line" style="top:403px">
      <svg width="10" height="10" viewBox="0 0 24 24"><path fill="var(--orange)" d="M6.6 10.8a15 15 0 0 0 6.6 6.6l2.2-2.2a1 1 0 0 1 1-.25 11.4 11.4 0 0 0 3.6.57 1 1 0 0 1 1 1V20a1 1 0 0 1-1 1A17 17 0 0 1 3 4a1 1 0 0 1 1-1h3.5a1 1 0 0 1 1 1c0 1.25.2 2.45.57 3.57a1 1 0 0 1-.25 1Z"/></svg>555-014-2200</p>
    <p class="contact-line" style="top:423px">
      <svg width="10" height="10" viewBox="0 0 24 24"><circle cx="12" cy="12" r="10" fill="none" stroke="var(--orange)" stroke-width="2.5"/><path d="M2 12h20M12 2c3 3 3 17 0 20M12 2c-3 3-3 17 0 20" fill="none" stroke="var(--orange)" stroke-width="2"/></svg>www.pinecrestcarehub.example</p>
  </section>

  <section class="panel-cover">
    <div class="logo">
      <span class="logo-dot"></span>
      <span class="logo-name">Pinecrest<br>Treatment Center</span>
    </div>
    <h1 class="cover-title"><span class="name">Pinecrest</span><span class="sub">TREATMENT CENTER</span></h1>
    <p class="cover-url">www.pinecrestcarehub.example</p>
  </section>
</main>
</body>
</html>
```